Cool one page design for outsource company in holland (just psd) UPDATE BRIEF

We are an internet agendy in holland and we outsource alot of our work.
Thats isnt always known. But now we want to launch a new label where clients can choose there own developer in the mosk known software frames like magento, wp, typo3, drupal, laravel etc.
We will select the best in the business and every developer comes with a project manager. So client can connect directly with the developer but still the work is checked by us and project is managed by us aswell in dutch. So if english isnt great, they an just do in dutch.
We want a creative but still a professional style site, so they arent dealing with an amateur organization.
We only want the psd, the rest of the coding we would do outselves. Or if you have coders aswell, we could add that as extra order.
Also there are some extra pages, we will pay for that later extra with the designer thats picked.
We have attached the logo and the brief
Good luck Guys!
Update:
We are getting very outdated design unfortanetely and very poorly worked out layouts.
To make it bit easier maybe it would be easier to use this theme as a basis:
https://taskora-demos.brimwell.com/extended/
We attached the theme aswell to this brief.
Maybe it would be better to customize this existing brief instead of making a totally new deisgn. Cause the custom design which are shown arent really up to standard im afraid.
We are getting really standard layout which arent really thought out, looks to much like copy paste work.
We need a clean but cool design and that hasnt been shown yet to us unfotanetely.
We havent seen any better layouts then this theme within this contest.
Often the desired sections are missing aswell:
Overview of developers, we can show a short number of developers displayed and then with a link show all devs, we can show the rest.
The how does it work section.
Also that section is integrated in this theme, but that can be more customized and look bit more neat, cause now the steps are to far apart and not well connected with eachother.
The steps:
1.
pick your developer
2.
Contact us with your needs
3.
You will be called by a projectmanager with
deadline and timeframe
4.
Work side by side with your developer
together with our project manager
5.
We use tools like Talkwave, Taskwell, Mail to get the work done
fast and within deadline.
It would also be cool to do some facts in the site like http://velqorapp.com/
Like
76% of the agencys outsources work to offshore anyway
74% of store owners arent satisfied with there current agency
64% of most skilled devs live in offshore countrys
Hope this helps to get the job done!
Reason: unfortanetely we get design from same designers only who seem to respond on every design contest. Low quality designs.
websites, webshop owners, agencys.
It Company
1 page
- clean look, prodessional, creative touch.
- wow factor
- boring and standard designs

```html
<!DOCTYPE html>
<html lang="en">
<head>
<meta charset="utf-8">
<title>Tidelane – your remote dev team</title>
<link rel="stylesheet" href="https://fonts.googleapis.com/css2?family=Open+Sans:ital,wght@0,400;0,600;0,700;1,400&family=Montserrat:wght@600;700&display=swap">
<style>
:root{
  --ink:#333a44;
  --muted:#7b828c;
  --navy:#1d3a5c;
  --blue:#0ea5ea;
  --blue-deep:#0b8fd6;
  --sky:#5aa8d6;
  --orange:#f7941d;
  --orange-deep:#f07a12;
  --hero:#dfe6ee;
  --pale:#dde4ec;
  --grey:#f4f4f4;
  --row:#e9ebed;
  --frame:#1f5f92;
  --footer:#3a3a3a;
  --footer-deep:#242424;
  --white:#fff;
}
*{box-sizing:border-box;margin:0;padding:0}
html,body{width:1200px;height:4775px;overflow:hidden}
body{font-family:"Open Sans",Arial,sans-serif;color:var(--ink);background:var(--white);position:relative}
section,header,footer{position:absolute;left:0;width:1200px;overflow:hidden}
.abs{position:absolute}

/* header */
.site-header{top:0;height:96px;background:var(--white)}
.brand{left:64px;top:26px}
.brand-name{font-family:"Montserrat",Arial,sans-serif;font-weight:700;font-size:27px;letter-spacing:1px;color:var(--navy);line-height:1}
.brand-tag{font-size:13px;color:var(--muted);letter-spacing:.5px;margin-top:4px}
.nav{right:0;top:0;height:96px;display:flex;align-items:center;padding-right:78px}
.nav a{font-size:15px;color:var(--ink);text-decoration:none;padding:0 20px;height:96px;line-height:104px}
.nav a.active{background:var(--hero)}

/* hero */
.hero{top:96px;height:563px;background:var(--hero)}
.hero-title{left:127px;top:190px;font-size:30px;font-weight:400;color:var(--ink)}
.hero-text{left:127px;top:246px;width:340px;font-size:13px;line-height:18px;color:var(--muted)}
.btn-orange{background:var(--orange);color:var(--white);font-size:12px;font-weight:600;text-align:center;text-transform:uppercase}
.hero-btn{left:197px;top:327px;width:147px;height:39px;line-height:39px}
.hero-art{left:525px;top:32px;width:653px;height:470px;border-radius:12px;background:radial-gradient(circle at 40% 40%,#f3f6f9,#c9d6e3 70%,var(--hero))}
.dots{left:566px;top:496px;display:flex;gap:8px}
.dots span{width:12px;height:12px;border-radius:50%;border:1px solid #a9b5c2}
.dots span.on{background:var(--sky);border-color:var(--sky)}

/* about */
.about{top:659px;height:430px;background:var(--white)}
.about-art{left:80px;top:56px;width:382px;height:302px;border-radius:10px;background:linear-gradient(160deg,#eef3f8,#d3e3ef)}
.about-title{left:551px;top:104px;font-size:30px;font-weight:400}
.about-text{left:551px;top:165px;width:560px;font-size:13px;line-height:18px;color:var(--muted)}
.btn-outline{left:551px;top:312px;width:108px;height:32px;border:1px solid #b7bcc2;font-size:11px;line-height:30px;text-align:center;color:var(--muted);text-transform:uppercase}

/* services */
.services{top:1089px;height:630px;background:#e9ecef}
.services-band{left:0;top:0;width:1200px;height:328px;background:linear-gradient(180deg,var(--orange),var(--orange-deep))}
.monitor{left:64px;top:89px;width:1072px;height:445px;background:var(--frame);border-radius:6px}
.monitor-screen{left:18px;top:18px;width:1036px;height:409px;background:#eef4f9}
.monitor-stand{width:398px;height:32px;background:#164a75;border-radius:0 0 16px 16px}
.services-title{left:0;width:1036px;top:60px;text-align:center;font-size:28px;font-weight:400;color:var(--ink)}
.bar{height:8px;border-radius:2px}
.service{top:155px;width:200px;text-align:center;font-size:20px;line-height:25px;color:var(--ink)}
.service svg{display:block;margin:0 auto 24px}
.service-sep{top:165px;width:1px;height:75px;background:#c7d3de}
.arrow{top:200px}

/* projects */
.projects-bar{top:1719px;height:89px;background:var(--sky)}
.projects-bar h2{position:absolute;left:105px;top:28px;font-size:25px;font-weight:400;color:var(--white)}
.projects{top:1808px;height:500px;background:var(--pale)}
.card{top:60px;width:286px}
.card-photo{width:286px;height:240px;border:4px solid var(--white);background:linear-gradient(135deg,#b9c5cf,#8d9aa6 55%,#d9dfe5);position:relative}
.card-caption{position:absolute;left:0;right:0;bottom:0;height:28px;background:rgba(183,216,240,.9);color:#2f7db8;font-size:13px;line-height:28px;text-align:center}
.card-text{margin-top:12px;font-size:11px;line-height:15px;color:var(--muted)}
.card-btn{margin-top:14px;width:64px;height:28px;line-height:28px;text-align:center;font-size:10px;color:var(--white);background:#a9aeb4;text-transform:uppercase}
.card-btn.first{background:#9fcbe8}

/* how it works */
.how{top:2308px;height:1098px;background:var(--grey)}
.how h2{position:absolute;left:105px;top:58px;font-size:28px;font-weight:400}
.step{left:64px;width:1069px;height:159px;background:var(--row)}
.step-num{left:57px;top:28px;width:104px;height:104px;border:6px solid var(--blue);border-radius:50%;text-align:center;line-height:92px;font-size:46px;color:var(--ink);background:var(--white)}
.step-brace{left:196px;top:30px;font-size:80px;line-height:90px;font-weight:400;color:var(--blue)}
.step-text{left:267px;width:760px;font-size:27px;line-height:36px;color:var(--ink)}
.contact-btn{left:834px;top:51px;width:184px;height:54px;line-height:54px;background:var(--blue);color:var(--white);font-size:15px;text-align:center;text-transform:uppercase}

/* facts */
.facts{top:3406px;height:582px;background:linear-gradient(180deg,var(--blue),var(--blue-deep))}
.facts h2{position:absolute;left:0;width:1200px;top:93px;text-align:center;font-size:30px;font-weight:700;color:var(--white)}
.facts-sub{left:0;width:1200px;top:142px;text-align:center;font-size:18px;color:var(--white)}
.fact{top:223px;width:380px;text-align:center;color:var(--white)}
.fact-ring{position:relative;width:190px;height:190px;margin:0 auto}
.fact-value{position:absolute;left:0;right:0;top:60px;font-family:"Montserrat",Arial,sans-serif;font-weight:700;font-size:54px;line-height:70px}
.fact-value small{font-size:28px}
.fact-label{margin-top:30px;font-size:18px;line-height:26px}

/* testimonials */
.testimonials{top:3988px;height:436px;background:var(--white)}
.testimonials h2{position:absolute;left:105px;top:86px;font-size:28px;font-weight:400}
.testimonials .rule{left:105px;top:141px;width:1000px;height:1px;background:#e1e1e1}
.quote{left:95px;top:191px;width:1003px;height:102px;background:#efefef;border-left:5px solid #8c8c8c}
.quote-mark{left:30px;top:12px;font-size:40px;color:#8c8c8c;font-family:Georgia,serif}
.quote-text{left:70px;top:24px;width:790px;font-style:italic;font-size:12px;line-height:18px;color:var(--muted)}
.avatar{left:981px;top:186px;width:114px;height:114px;border-radius:50%;border:5px solid var(--blue);background:linear-gradient(180deg,#c9ced4,#6f7882)}
.author{right:110px;top:318px;font-style:italic;font-size:15px;color:var(--blue-deep)}

/* footer */
.site-footer{top:4424px;height:351px;background:var(--footer);color:var(--white)}
.footer-col h3{font-size:20px;font-weight:400}
.footer-sep{top:66px;width:1px;height:150px;background:#555}
.news-input{left:99px;top:118px;width:261px;height:45px;background:var(--white);font-size:13px;color:#aaa;line-height:45px;padding-left:14px}
.news-btn{left:264px;top:172px;width:96px;height:35px;line-height:35px;background:var(--blue);font-size:12px;text-align:center;text-transform:uppercase}
.contact-lines{font-size:16px;line-height:30px}
.contact-lines strong{font-weight:700;letter-spacing:.5px}
.social{left:885px;top:124px;display:flex;gap:38px}
.social span{width:32px;height:32px;border-radius:50%;border:3px solid var(--white)}
.copyright{left:0;top:293px;width:1200px;height:58px;background:var(--footer-deep);font-size:16px;line-height:58px;padding-left:99px}
</style>
</head>
<body>

<header class="site-header">
  <div class="abs brand">
    <div class="brand-name">TIDELANE</div>
    <div class="brand-tag">your remote dev team</div>
  </div>
  <nav class="abs nav">
    <a class="active" href="#">Home</a>
    <a href="#">About</a>
    <a href="#">Services</a>
    <a href="#">How it works</a>
    <a href="#">Blog</a>
    <a href="#">Contact</a>
  </nav>
</header>

<section class="hero">
  <h1 class="abs hero-title">Website Development</h1>
  <p class="abs hero-text">Lorem Ipsum is simply dummy text of the printing and typesetting industry. Lorem Ipsum has been the standard dummy text for a gallery of type book.</p>
  <div class="abs btn-orange hero-btn">Learn more</div>
  <div class="abs hero-art" role="img" aria-label="Illustration of a laptop, a notice board and web technology badges connected by pipes"></div>
  <div class="abs dots"><span class="on"></span><span></span><span></span><span></span></div>
</section>

<section class="about">
  <div class="abs about-art" role="img" aria-label="Illustration of a laptop showing code with a paper plane flying out"></div>
  <h2 class="abs about-title">About Us</h2>
  <p class="abs about-text">Lorem Ipsum is simply dummy text of the printing and typesetting industry. Lorem Ipsum has been the industry's standard dummy text ever since the 1500s, when an unknown printer took a galley of type and scrambled it to make a type specimen book. It has survived not only five centuries, but also the leap into electronic typesetting, remaining essentially unchanged. It was popularised in the 1960s with the release of sheets containing passages, and more recently with desktop publishing versions of Lorem Ipsum.</p>
  <div class="abs btn-outline">Read more</div>
</section>

<section class="services">
  <div class="abs services-band" role="img" aria-label="Orange band with a faint pattern of office and technology icons"></div>
  <div class="abs monitor">
    <div class="abs monitor-screen">
      <div class="abs bar" style="left:25px;top:28px;width:200px;background:#d9422b"></div>
      <div class="abs bar" style="left:25px;top:50px;width:290px;background:var(--orange)"></div>
      <div class="abs bar" style="left:25px;top:72px;width:90px;background:var(--sky)"></div>
      <div class="abs bar" style="left:705px;top:28px;width:300px;background:#d9422b"></div>
      <div class="abs bar" style="left:600px;top:50px;width:405px;background:var(--sky)"></div>
      <div class="abs bar" style="left:935px;top:72px;width:70px;background:var(--sky)"></div>
      <h2 class="abs services-title">Services</h2>

      <svg class="abs arrow" style="left:25px" width="24" height="40" viewBox="0 0 24 40"><path d="M20 4 4 20l16 16" fill="none" stroke="#333a44" stroke-width="3"/></svg>
      <svg class="abs arrow" style="left:990px" width="24" height="40" viewBox="0 0 24 40"><path d="M4 4l16 16L4 36" fill="none" stroke="#333a44" stroke-width="3"/></svg>

      <div class="abs service" style="left:60px">
        <svg width="80" height="72" viewBox="0 0 80 72"><rect x="8" y="8" width="64" height="42" rx="3" fill="none" stroke="#1c8fd1" stroke-width="4"/><path d="M32 50v10h16V50M24 64h32" stroke="#1c8fd1" stroke-width="4" fill="none"/><path d="M30 40l22-22" stroke="#1c8fd1" stroke-width="4"/></svg>
        Design &amp;<br>Multimedia
      </div>
      <div class="abs service-sep" style="left:282px"></div>
      <div class="abs service" style="left:302px">
        <svg width="80" height="72" viewBox="0 0 80 72"><rect x="8" y="14" width="60" height="44" rx="3" fill="none" stroke="#1c8fd1" stroke-width="4"/><text x="38" y="44" text-anchor="middle" font-family="Open Sans,Arial,sans-serif" font-size="15" font-weight="700" fill="#1c8fd1">www</text><circle cx="66" cy="14" r="8" fill="#1c8fd1"/></svg>
        Website<br>Development
      </div>
      <div class="abs service-sep" style="left:520px"></div>
      <div class="abs service" style="left:540px">
        <svg width="80" height="72" viewBox="0 0 80 72"><text x="40" y="56" text-anchor="middle" font-family="Open Sans,Arial,sans-serif" font-size="56" fill="#1c8fd1">{/}</text></svg>
        Programming &amp;<br>IT
      </div>
      <div class="abs service-sep" style="left:758px"></div>
      <div class="abs service" style="left:778px">
        <svg width="80" height="72" viewBox="0 0 80 72"><rect x="8" y="12" width="64" height="48" rx="3" fill="none" stroke="#1c8fd1" stroke-width="4"/><path d="M8 22h64" stroke="#1c8fd1" stroke-width="4"/><path d="M30 32l-8 8 8 8M50 32l8 8-8 8M44 30l-8 20" fill="none" stroke="#1c8fd1" stroke-width="3"/></svg>
        Software<br>Development
      </div>
    </div>
  </div>
  <div class="abs monitor-stand" style="left:398px;top:534px"></div>
</section>

<section class="projects-bar">
  <h2>Recent Projects</h2>
  <svg class="abs" style="left:1036px;top:30px" width="60" height="30" viewBox="0 0 60 30"><path d="M14 5 4 15l10 10M46 5l10 10-10 10" fill="none" stroke="#fff" stroke-width="3"/></svg>
</section>

<section class="projects">
  <div class="abs card" style="left:105px">
    <div class="card-photo" role="img" aria-label="Photo of a business team shaking hands in an office"><div class="card-caption">Lorem Ipsum simply dummy</div></div>
    <p class="card-text">Lorem Ipsum is simply dummy text of the printing and typesetting industry. Lorem Ipsum has been when an unknown printer took a galley of type and scrambled it to make a type specimen book.</p>
    <div class="card-btn first">More</div>
  </div>
  <div class="abs card" style="left:452px">
    <div class="card-photo" role="img" aria-label="Photo of a business team shaking hands in an office"><div class="card-caption">Lorem Ipsum simply dummy</div></div>
    <p class="card-text">Lorem Ipsum is simply dummy text of the printing and typesetting industry. Lorem Ipsum has been when an unknown printer took a galley of type and scrambled it to make a type specimen book.</p>
    <div class="card-btn">More</div>
  </div>
  <div class="abs card" style="left:802px">
    <div class="card-photo" role="img" aria-label="Photo of a business team shaking hands in an office"><div class="card-caption">Lorem Ipsum simply dummy</div></div>
    <p class="card-text">Lorem Ipsum is simply dummy text of the printing and typesetting industry. Lorem Ipsum has been when an unknown printer took a galley of type and scrambled it to make a type specimen book.</p>
    <div class="card-btn">More</div>
  </div>
</section>

<section class="how">
  <h2>How it works?</h2>
  <div class="abs step" style="top:137px">
    <div class="abs step-num">1</div><div class="abs step-brace">{</div>
    <p class="abs step-text" style="top:62px">pick your developer</p>
  </div>
  <div class="abs step" style="top:315px">
    <div class="abs step-num">2</div><div class="abs step-brace">{</div>
    <p class="abs step-text" style="top:62px">Contact us with your needs</p>
    <div class="abs contact-btn">Contact us</div>
  </div>
  <div class="abs step" style="top:493px">
    <div class="abs step-num">3</div><div class="abs step-brace">{</div>
    <p class="abs step-text" style="top:44px">You will be called by a projectmanager with deadline and timeframe</p>
  </div>
  <div class="abs step" style="top:668px">
    <div class="abs step-num">4</div><div class="abs step-brace">{</div>
    <p class="abs step-text" style="top:44px">Work side by side with your developer together with our project manager</p>
  </div>
  <div class="abs step" style="top:846px">
    <div class="abs step-num">5</div><div class="abs step-brace">{</div>
    <p class="abs step-text" style="top:44px">We use tools like Talkwave, Taskwell, Mail to get the work done fast and within deadline.</p>
  </div>
</section>

<section class="facts">
  <h2>The hard truth</h2>
  <p class="abs facts-sub">It is a long established fact that a reader will be distracted</p>
  <div class="abs fact" style="left:49px">
    <div class="fact-ring">
      <svg width="190" height="190" viewBox="0 0 190 190"><circle cx="95" cy="95" r="85" fill="none" stroke="rgba(255,255,255,.35)" stroke-width="14"/><circle cx="95" cy="95" r="85" fill="none" stroke="#fff" stroke-width="14" stroke-dasharray="406 534" transform="rotate(-90 95 95)"/></svg>
      <div class="fact-value">76<small>%</small></div>
    </div>
    <p class="fact-label">of the agencys outsources work<br>to offshore anyway</p>
  </div>
  <div class="abs fact" style="left:399px">
    <div class="fact-ring">
      <svg width="190" height="190" viewBox="0 0 190 190"><circle cx="95" cy="95" r="85" fill="none" stroke="rgba(255,255,255,.35)" stroke-width="14"/><circle cx="95" cy="95" r="85" fill="none" stroke="#fff" stroke-width="14" stroke-dasharray="395 534" transform="rotate(-90 95 95)"/></svg>
      <div class="fact-value">74<small>%</small></div>
    </div>
    <p class="fact-label">of store owners arent satisfied<br>with there current agency</p>
  </div>
  <div class="abs fact" style="left:749px">
    <div class="fact-ring">
      <svg width="190" height="190" viewBox="0 0 190 190"><circle cx="95" cy="95" r="85" fill="none" stroke="rgba(255,255,255,.35)" stroke-width="14"/><circle cx="95" cy="95" r="85" fill="none" stroke="#fff" stroke-width="14" stroke-dasharray="342 534" transform="rotate(-90 95 95)"/></svg>
      <div class="fact-value">64<small>%</small></div>
    </div>
    <p class="fact-label">of most skilled devs live in<br>offshore countrys</p>
  </div>
</section>

<section class="testimonials">
  <h2>Testimonials</h2>
  <div class="abs rule"></div>
  <div class="abs quote">
    <div class="abs quote-mark">“</div>
    <p class="abs quote-text">Lorem Ipsum is simply dummy text of the printing and typesetting industry. Lorem Ipsum has been the industry's standard dummy text ever since the 1500s, when an unknown printer took a galley of type and scrambled it to make a type specimen book. It has survived not only five centuries, but also the leap into electronic typesetting.</p>
  </div>
  <div class="abs avatar" role="img" aria-label="Portrait photo of the client"></div>
  <p class="abs author">Pieter Vermaas - CEO Noordkant Media</p>
</section>

<footer class="site-footer">
  <div class="abs footer-col" style="left:99px;top:70px"><h3>Newsletter</h3></div>
  <div class="abs news-input">Email address</div>
  <div class="abs news-btn">Subscribe</div>
  <div class="abs footer-sep" style="left:477px"></div>
  <div class="abs footer-col" style="left:541px;top:70px">
    <h3>Contact Us</h3>
    <div class="contact-lines" style="margin-top:18px">
      <strong>TIDELANE</strong><br>T: 020-555-0147<br>E: info@tidelane.com
    </div>
  </div>
  <div class="abs footer-sep" style="left:821px"></div>
  <div class="abs footer-col" style="left:885px;top:70px"><h3>Social Media</h3></div>
  <div class="abs social" aria-label="Social media links"><span></span><span></span><span></span><span></span></div>
  <div class="abs copyright">Copyrights 2016 tidelane. All Rights Reserved</div>
</footer>

</body>
</html>
```